Bakery and cafe
Savor Every Crumb Now
Project: Bakery and cafe
Bakery and cafe -
Creative Brief
Use specific fonts
Classy, elegant, close to logo font
Bright & Fun-filled
Harlowe
Owner
1785 Brookvale dr Atlanta, Ga. 30318
jmharlowe@hqbakeryandcafe.example
www.hqbakeryandcafe.example
want both vertical and horizontal draft. Really want a vertical card.
Logo in black and white. or gray scale depending on the color of the front and the actual card.

```html
<!DOCTYPE html>
<html lang="en">
<head>
<meta charset="utf-8">
<title>HQ Bakery &amp; Cafe – Stationery</title>
<link rel="stylesheet" href="https://fonts.googleapis.com/css2?family=Cormorant+Garamond:wght@700&family=Great+Vibes&family=Open+Sans:wght@400;600&display=swap">
<style>
  :root {
    --brown: #6a2816;
    --brown-dark: #521d0f;
    --cream-light: #fffbe8;
    --cream: #fbefc0;
    --cream-deep: #f2d98a;
    --accent-red: #c4271c;
    --paper: #ffffff;
    --faint: #f1ece6;
    --ink: #3b2a22;
    --backdrop: #e6e6e6;
  }
  * { margin: 0; padding: 0; box-sizing: border-box; }
  html, body { width: 1200px; height: 847px; overflow: hidden; }
  body {
    background: radial-gradient(ellipse at 50% 45%, #f4f4f4 0%, var(--backdrop) 75%);
    font-family: "Open Sans", Arial, sans-serif;
    color: var(--ink);
    position: relative;
  }
  .piece { position: absolute; box-shadow: 0 2px 6px rgba(0,0,0,.25); overflow: hidden; }

  /* Brand block */
  .brand-panel {
    position: absolute;
    background: linear-gradient(180deg, var(--cream-light) 0%, var(--cream) 55%, var(--cream-deep) 100%);
    display: flex; flex-direction: column; align-items: center; justify-content: center;
    text-align: center;
  }
  .brand-dot { border-radius: 50%; background: var(--accent-red); }
  .brand-name {
    font-family: "Cormorant Garamond", Georgia, serif;
    font-weight: 700; color: var(--brown); line-height: 1.05; letter-spacing: .5px;
  }
  .brand-tagline { font-family: "Great Vibes", cursive; color: var(--brown); line-height: 1; }

  .watermark {
    position: absolute; font-family: "Cormorant Garamond", Georgia, serif; font-weight: 700;
    color: var(--faint); text-align: center; line-height: 1;
  }

  /* Envelope back */
  .envelope-back { left: 31px; top: 67px; width: 586px; height: 137px; background: #f7f4ee; }
  .envelope-back .flap { position: absolute; inset: 0; }
  .envelope-back .flap-url {
    position: absolute; top: 12px; width: 100%; text-align: center;
    font-size: 7px; letter-spacing: 2px; color: #e9c9a4;
  }

  /* Envelope front */
  .envelope-front { left: 65px; top: 163px; width: 576px; height: 281px; background: var(--paper); }
  .envelope-front .brand-panel { left: 9px; top: 5px; width: 125px; height: 151px; }
  .envelope-front .brand-dot { width: 18px; height: 18px; margin-bottom: 8px; }
  .envelope-front .brand-name { font-size: 19px; }
  .envelope-front .brand-tagline { font-size: 14px; margin-top: 4px; }
  .envelope-front .watermark { left: 250px; top: 60px; font-size: 120px; }
  .envelope-front .address { position: absolute; left: 9px; top: 242px; font-size: 7px; }
  .envelope-front .band { position: absolute; left: 0; right: 0; bottom: 5px; height: 14px; background: var(--brown); }

  /* Letterhead */
  .letterhead { left: 619px; top: 29px; width: 545px; height: 787px; background: var(--paper); }
  .letterhead .brand-panel { left: 84px; top: 0; width: 108px; height: 199px; }
  .letterhead .brand-dot { width: 20px; height: 20px; margin-bottom: 10px; }
  .letterhead .brand-name { font-size: 17px; }
  .letterhead .brand-tagline { font-size: 14px; margin-top: 5px; }
  .letterhead .watermark { left: 40px; width: 480px; top: 300px; font-size: 210px; }
  .letterhead .contact {
    position: absolute; left: 0; right: 0; top: 752px; text-align: center; font-size: 7px; line-height: 1.5;
  }
  .letterhead .contact .url { letter-spacing: 1.5px; }
  .letterhead .band { position: absolute; left: 0; right: 0; bottom: 4px; height: 9px; background: var(--brown); }

  /* Business card back */
  .card-back { left: 79px; top: 454px; width: 207px; height: 364px; background: var(--brown); }
  .card-back .watermark { color: rgba(255,255,255,.07); left: 0; width: 100%; top: 40px; font-size: 130px; }
  .card-back .emblem { position: absolute; left: 0; width: 100%; top: 140px; display: flex; flex-direction: column; align-items: center; }
  .card-back .brand-dot { width: 16px; height: 16px; margin-bottom: 8px; }
  .card-back .brand-name { color: var(--cream-deep); font-size: 17px; text-align: center; }
  .card-back .url { position: absolute; bottom: 20px; width: 100%; text-align: center; font-size: 7px; letter-spacing: 1px; color: #e9c9a4; }

  /* Business card front */
  .card-front { left: 305px; top: 454px; width: 211px; height: 364px; background: var(--brown); }
  .card-front .brand-panel { left: 0; top: 0; width: 100%; height: 134px; }
  .card-front .brand-dot { width: 18px; height: 18px; margin-bottom: 8px; }
  .card-front .brand-name { font-size: 20px; }
  .card-front .brand-tagline { font-size: 15px; margin-top: 4px; }
  .card-front .details { position: absolute; left: 0; right: 0; top: 150px; text-align: center; color: var(--cream); font-size: 7.5px; line-height: 1.45; }
  .card-front .person { font-family: "Cormorant Garamond", Georgia, serif; font-weight: 700; font-size: 17px; color: var(--cream-deep); }
  .card-front .role { font-size: 6.5px; margin-bottom: 14px; }
  .card-front .label { font-weight: 600; margin-top: 6px; }
</style>
</head>
<body>

  <section class="piece envelope-back" aria-label="Envelope back">
    <svg class="flap" viewBox="0 0 586 137" preserveAspectRatio="none" aria-hidden="true">
      <rect x="0" y="0" width="586" height="6" fill="#f2dfa6"/>
      <polygon points="0,6 586,6 293,137" fill="#6a2816"/>
    </svg>
    <p class="flap-url">www.hqbakeryandcafe.example</p>
  </section>

  <section class="piece envelope-front" aria-label="Envelope front">
    <div class="watermark" aria-hidden="true">HQ</div>
    <div class="brand-panel">
      <span class="brand-dot"></span>
      <span class="brand-name">HQ Bakery<br>&amp; Cafe</span>
      <span class="brand-tagline">Savor Every Crumb Now</span>
    </div>
    <p class="address">1785 Brookvale dr Atlanta, Ga. 30318</p>
    <div class="band"></div>
  </section>

  <section class="piece letterhead" aria-label="Letterhead">
    <div class="watermark" aria-hidden="true">HQ</div>
    <div class="brand-panel">
      <span class="brand-dot"></span>
      <span class="brand-name">HQ Bakery<br>&amp; Cafe</span>
      <span class="brand-tagline">Savor Every Crumb Now</span>
    </div>
    <div class="contact">
      <p>1785 Brookvale dr Atlanta, Ga. 30318</p>
      <p>Cell 5550142291 · Email jmharlowe@hqbakeryandcafe.example</p>
      <p class="url">www.hqbakeryandcafe.example</p>
    </div>
    <div class="band"></div>
  </section>

  <section class="piece card-back" aria-label="Business card back">
    <div class="watermark" aria-hidden="true">HQ</div>
    <div class="emblem">
      <span class="brand-dot"></span>
      <span class="brand-name">HQ Bakery<br>&amp; Cafe</span>
    </div>
    <p class="url">www.hqbakeryandcafe.example</p>
  </section>

  <section class="piece card-front" aria-label="Business card front">
    <div class="brand-panel">
      <span class="brand-dot"></span>
      <span class="brand-name">HQ Bakery &amp; Cafe</span>
      <span class="brand-tagline">Savor Every Crumb Now</span>
    </div>
    <div class="details">
      <p class="person">Harlowe</p>
      <p class="role">Owner</p>
      <p>1785 Brookvale dr Atlanta, Ga. 30318</p>
      <p class="label">Cell</p>
      <p>5550142291</p>
      <p class="label">Email</p>
      <p>jmharlowe@hqbakeryandcafe.example</p>
    </div>
  </section>

</body>
</html>
```